Corvane ridgewell mechanical

I want a full wrap other than the top of the van.
My services include hvac central A/C, heat pumps,
Fresh air systems, as well as beer and soda systems, air compressors and cryogenics. I have a 2013 Talvor kx 3100 van high roof

Residential and commercial

HVAC , air compressors, beer and soda systems

• Image or design that stands out. Looks sleek and original

```html
<!DOCTYPE html>
<html lang="en">
<head>
<meta charset="utf-8">
<title>Corvane Ridgewell Mechanical – Side Wrap</title>
<link rel="stylesheet" href="https://fonts.googleapis.com/css2?family=Montserrat:wght@600;700;800&display=swap">
<style>
  :root {
    --navy: #0f2a9a;
    --deep-navy: #0a1f86;
    --wrap-red: #e0140f;
    --accent-blue: #3a6fe0;
    --ink: #111111;
    --wrap-white: #f6f4ee;
    --backdrop: #e4e7ea;
  }
  * { margin: 0; padding: 0; box-sizing: border-box; }
  html, body { width: 1200px; height: 1000px; overflow: hidden; background: var(--backdrop); }
  .canvas { position: relative; width: 1200px; height: 1000px; font-family: "Montserrat", sans-serif; }
  .wrap-art { position: absolute; left: 0; top: 0; }
  .brand-dot { position: absolute; border-radius: 50%; background: var(--deep-navy); }
  .main-dot { left: 581px; top: 300px; width: 92px; height: 92px; }
  .brand-name { position: absolute; color: var(--navy); font-weight: 800; text-transform: uppercase; white-space: nowrap; text-align: right; }
  .brand-name span { display: block; }
  .main-name { left: 700px; top: 306px; width: 322px; }
  .main-name .name-first { font-size: 27px; line-height: 32px; }
  .main-name .name-second { font-size: 21px; line-height: 25px; }
  .tagline { position: absolute; color: var(--ink); font-weight: 700; text-transform: uppercase; white-space: nowrap; }
  .main-tagline { left: 700px; top: 364px; width: 322px; font-size: 19.5px; line-height: 22px; text-align: right; }
  .service-list { position: absolute; left: 700px; top: 400px; list-style: none; color: var(--navy); font-weight: 700; font-size: 16px; line-height: 20.5px; }
  .service-list li::before { content: "• "; }
  .door-name { left: 326px; top: 540px; width: 208px; }
  .door-name .name-first { font-size: 16.5px; line-height: 20px; }
  .door-name .name-second { font-size: 14px; line-height: 17px; }
  .door-tagline { left: 326px; top: 578px; width: 208px; font-size: 10.5px; line-height: 12px; text-align: right; }
  .door-phone { position: absolute; left: 326px; top: 590px; width: 208px; color: var(--wrap-red); font-weight: 800; font-size: 29px; line-height: 32px; text-align: right; white-space: nowrap; }
</style>
</head>
<body>
<div class="canvas">
  <svg class="wrap-art" width="1200" height="1000" viewBox="0 0 1200 1000" aria-hidden="true">
    <rect class="wrap-panel" x="20" y="225" width="1160" height="480" rx="14" fill="var(--wrap-white)"/>
    <path class="red-swoosh" d="M1043 225 C1110 330 1085 520 880 600 C690 670 460 664 300 664 L300 705 L1166 705 Q1180 705 1180 691 L1180 239 Q1180 225 1166 225 Z" fill="var(--wrap-red)"/>
    <path class="blue-sweep" d="M285 648 C520 652 760 620 900 548 C1010 490 1062 390 1062 282" fill="none" stroke="var(--accent-blue)" stroke-width="5" stroke-linecap="round"/>
  </svg>

  <span class="brand-dot main-dot"></span>
  <p class="brand-name main-name"><span class="name-first">Corvane Ridgewell</span><span class="name-second">Mechanical</span></p>
  <p class="tagline main-tagline">Be proactive not reactive</p>
  <ul class="service-list">
    <li>Restaurants &amp; Bar Equipment</li>
    <li>Beer &amp; Soda Systems</li>
    <li>Air Compressor/Dryers</li>
    <li>IAQ Testing &amp; Monitoring</li>
    <li>Piping &amp; Heat Pumps</li>
    <li>HVAC Services</li>
    <li>Cryogenics</li>
  </ul>

  <p class="brand-name door-name"><span class="name-first">Corvane Ridgewell</span><span class="name-second">Mechanical</span></p>
  <p class="tagline door-tagline">Be proactive not reactive</p>
  <p class="door-phone">802-555-0147</p>
</div>
</body>
</html>
```